Plumerly Ad for “7 Step Signature Presence Sprint”

I would like a Plumerly ad graphic for this offer:
https://www.morvindeals.net/7-step-signature-presence-sprint
Please include my photo- I have attached images to use (remove the background)
The big selling points are the three focus points during the challenge (Plumerly Page, Taskvane profile and the web site) and the cost is only $5.40
I will choose the winner who submits one ad, and then the winner will be asked to provide two variations of the ad graphic so I can test all three graphics.
Thank you, I’m looking forward to seeing your ideas and designs!

```html
<!DOCTYPE html>
<html lang="en">
<head>
<meta charset="utf-8">
<title>7 Step Signature Presence Sprint – Plumerly Ad</title>
<link rel="stylesheet" href="https://fonts.googleapis.com/css2?family=Bebas+Neue&family=Great+Vibes&family=Oswald:wght@500;600&display=swap">
<style>
  :root {
    --blue: #1348d6;
    --blue-deep: #0b36b8;
    --blue-mid: #2f6fe6;
    --blue-light: #6fa9f2;
    --sky: #e9eef6;
    --white: #ffffff;
    --ink: #0f47d0;
  }
  * { margin: 0; padding: 0; box-sizing: border-box; }
  html, body { width: 1200px; height: 1200px; overflow: hidden; background: var(--white); }
  .ad {
    position: relative;
    width: 1200px;
    height: 1200px;
    overflow: hidden;
    font-family: "Oswald", sans-serif;
  }
  .ad__backdrop { position: absolute; inset: 0; }
  .headline-number {
    position: absolute;
    left: 70px; top: 40px;
    font-family: "Bebas Neue", sans-serif;
    font-size: 300px;
    line-height: 1;
    color: var(--ink);
    letter-spacing: 2px;
  }
  .headline-number .outline {
    color: var(--blue-deep);
    -webkit-text-stroke: 8px var(--white);
    paint-order: stroke fill;
  }
  .headline-topic {
    position: absolute;
    right: 80px; top: 62px;
    font-family: "Bebas Neue", sans-serif;
    font-size: 118px;
    line-height: 0.98;
    color: var(--ink);
    text-align: center;
  }
  .headline-script {
    position: absolute;
    right: 90px; top: 300px;
    font-family: "Great Vibes", cursive;
    font-size: 190px;
    line-height: 1;
    color: var(--blue);
  }
  .portrait {
    position: absolute;
    left: -50px; top: 510px;
    width: 790px; height: 790px;
  }
  .price-badge {
    position: absolute;
    left: 790px; top: 603px;
    width: 324px; height: 324px;
    border-radius: 50%;
    background: var(--white);
    border: 8px solid var(--blue);
    display: flex; flex-direction: column;
    align-items: center; justify-content: center;
    color: var(--ink);
    font-weight: 600;
    font-size: 84px;
    line-height: 1.05;
  }
  .brand-mark {
    position: absolute;
    left: 820px; top: 1030px;
    display: flex; align-items: center; gap: 16px;
    color: var(--white);
    font-weight: 500;
    font-size: 38px;
    letter-spacing: 1px;
  }
  .brand-mark__dot {
    width: 46px; height: 46px;
    border-radius: 50%;
    background: var(--white);
  }
</style>
</head>
<body>
<div class="ad">
  <svg class="ad__backdrop" width="1200" height="1200" viewBox="0 0 1200 1200">
    <defs>
      <linearGradient id="deepBlue" x1="0" y1="0" x2="1" y2="1">
        <stop offset="0" stop-color="#1f5fe0"/>
        <stop offset="1" stop-color="#0b34c2"/>
      </linearGradient>
      <linearGradient id="paleBand" x1="0" y1="0" x2="1" y2="1">
        <stop offset="0" stop-color="#ffffff"/>
        <stop offset="0.6" stop-color="#e6ecf5"/>
        <stop offset="1" stop-color="#c4d8f4"/>
      </linearGradient>
    </defs>
    <rect width="1200" height="1200" fill="url(#deepBlue)"/>
    <polygon points="0,0 360,0 120,420 0,520" fill="#4a8ff0" opacity="0.55"/>
    <polygon points="0,60 240,0 40,330 0,360" fill="#7ab6f6" opacity="0.5"/>
    <polygon points="180,0 1200,0 1200,1010 560,580 300,260" fill="url(#paleBand)"/>
    <polygon points="560,580 1200,1010 1200,1080 520,640" fill="#8cbaf2" opacity="0.7"/>
  </svg>

  <div class="headline-number"><span class="outline">7</span> STEP</div>
  <div class="headline-topic">SIGNATURE<br>PRESENCE</div>
  <div class="headline-script">Sprint!</div>

  <svg class="portrait" viewBox="0 0 790 790" role="img" aria-label="Photo of the host, seated and smiling, background removed">
    <defs>
      <linearGradient id="portraitTone" x1="0" y1="0" x2="0" y2="1">
        <stop offset="0" stop-color="#3a3f4a"/>
        <stop offset="1" stop-color="#1b1f2a"/>
      </linearGradient>
    </defs>
    <circle cx="395" cy="395" r="388" fill="#ffffff" stroke="#1348d6" stroke-width="10"/>
    <circle cx="395" cy="395" r="370" fill="url(#portraitTone)" opacity="0.85"/>
  </svg>

  <div class="price-badge"><span>ONLY</span><span>$5.40</span></div>

  <div class="brand-mark">
    <span class="brand-mark__dot"></span>
    <span class="brand-mark__name">KESTROW GROUP</span>
  </div>
</div>
</body>
</html>
```